Harlow Hauling | ||
Fine furniture transport and delivery service | ||
Use same font as used in my logo | ||
Cutting-Edge Modern Bright & Fun-filled |
Danny Crebbe | ||
Owner | ||
5810 County Road 7 Canaan,NH 03598 |
pinecarrier@velmorapost.net | ||
Looking for something that stands out. Maybe photo shop my logo into a 2008 or newer Korvath trekline van. | ||

```html
<!DOCTYPE html>
<html lang="en">
<head>
<meta charset="utf-8">
<title>Harlow Hauling — Stationery Set</title>
<link href="https://fonts.googleapis.com/css2?family=Exo+2:wght@400;700&display=swap" rel="stylesheet">
<style>
  :root {
    --green: #35e32f;
    --green-deep: #1b9d18;
    --charcoal: #3a3d3f;
    --charcoal-dark: #2b2d2f;
    --paper: #ffffff;
    --ink: #4a4a4a;
    --stage: #d6d7d8;
    --ghost: rgba(60, 120, 60, 0.08);
  }
  * { box-sizing: border-box; margin: 0; padding: 0; }
  html, body { width: 1200px; height: 324px; overflow: hidden; }
  body {
    background: var(--stage);
    font-family: "Exo 2", sans-serif;
    color: var(--ink);
    position: relative;
  }
  .sheet { position: absolute; background: var(--paper); overflow: hidden; box-shadow: 0 1px 3px rgba(0,0,0,.25); }
  .sheet--dark { background: var(--charcoal); }
  .wave { position: absolute; left: 0; bottom: 0; width: 100%; }
  .brand { display: flex; align-items: center; gap: 4px; font-weight: 700; color: var(--green-deep); white-space: nowrap; }
  .brand__dot { width: 1em; height: 1em; border-radius: 50%; background: var(--green); flex: none; }
  .sheet--dark .brand { color: var(--green); }
  .tagline { font-size: 3px; color: #888; }
  .contact { font-size: 3.6px; line-height: 1.5; color: var(--ink); }
  .ghost-mark {
    position: absolute; border-radius: 50%; background: var(--ghost);
    display: flex; align-items: center; justify-content: center;
    color: rgba(60, 120, 60, 0.12); font-weight: 700;
  }
  .flap { position: absolute; left: 0; top: 0; width: 100%; }
</style>
</head>
<body>

<!-- Business card: front -->
<div class="sheet business-card" style="left:28px;top:34px;width:88px;height:52px;">
  <div class="brand" style="position:absolute;left:6px;top:6px;font-size:6px;">
    <span class="brand__dot"></span>Harlow Hauling
  </div>
  <div class="contact" style="position:absolute;right:6px;top:20px;text-align:right;">
    <strong>Danny Crebbe</strong><br>Owner<br>603-555-0147
  </div>
  <svg class="wave" viewBox="0 0 88 12" height="12" preserveAspectRatio="none">
    <path d="M0 6 Q30 0 88 5 V12 H0Z" fill="var(--green)"/>
    <path d="M0 9 Q40 4 88 8 V12 H0Z" fill="var(--charcoal)"/>
  </svg>
</div>

<!-- Business card: back -->
<div class="sheet sheet--dark business-card" style="left:28px;top:98px;width:88px;height:52px;">
  <div class="brand" style="position:absolute;left:50%;top:18px;transform:translateX(-50%);font-size:6px;">
    <span class="brand__dot"></span>Harlow Hauling
  </div>
  <svg class="wave" viewBox="0 0 88 10" height="10" preserveAspectRatio="none">
    <path d="M0 6 Q44 0 88 6 V10 H0Z" fill="var(--green)"/>
  </svg>
</div>

<!-- Business card: alternate back -->
<div class="sheet sheet--dark business-card" style="left:28px;top:162px;width:88px;height:52px;background:var(--charcoal-dark);">
  <div class="brand" style="position:absolute;left:50%;top:22px;transform:translateX(-50%);font-size:6px;">
    <span class="brand__dot"></span>Harlow Hauling
  </div>
</div>

<!-- Large brand lockup -->
<div class="brand" style="position:absolute;left:8px;top:250px;font-size:11px;">
  <span class="brand__dot"></span>Harlow Hauling
</div>

<!-- Letterhead 1 -->
<div class="sheet letterhead" style="left:233px;top:19px;width:150px;height:212px;">
  <div class="brand" style="position:absolute;left:12px;top:12px;font-size:5.5px;">
    <span class="brand__dot"></span>Harlow Hauling
  </div>
  <div class="contact" style="position:absolute;right:12px;top:10px;text-align:right;font-size:3px;">
    5810 County Road 7<br>Canaan, NH 03598<br>pinecarrier@velmorapost.net
  </div>
  <div class="ghost-mark" style="left:40px;top:60px;width:70px;height:70px;font-size:7px;">Harlow Hauling</div>
  <svg class="wave" viewBox="0 0 150 22" height="22" preserveAspectRatio="none">
    <path d="M0 12 Q60 0 150 10 V22 H0Z" fill="var(--green)"/>
    <path d="M0 17 Q70 8 150 15 V22 H0Z" fill="var(--charcoal)"/>
  </svg>
</div>

<!-- Letterhead 2 -->
<div class="sheet letterhead" style="left:451px;top:19px;width:150px;height:212px;">
  <div class="brand" style="position:absolute;left:12px;top:12px;font-size:5.5px;">
    <span class="brand__dot"></span>Harlow Hauling
  </div>
  <div class="contact" style="position:absolute;right:12px;top:10px;text-align:right;font-size:3px;">
    5810 County Road 7<br>Canaan, NH 03598<br>pinecarrier@velmorapost.net
  </div>
  <div class="ghost-mark" style="left:40px;top:60px;width:70px;height:70px;font-size:7px;">Harlow Hauling</div>
  <svg class="wave" viewBox="0 0 150 22" height="22" preserveAspectRatio="none">
    <path d="M0 12 Q60 0 150 10 V22 H0Z" fill="var(--green)"/>
    <path d="M0 17 Q70 8 150 15 V22 H0Z" fill="var(--charcoal)"/>
  </svg>
</div>

<!-- Compliment slip 1 -->
<div class="sheet compliment-slip" style="left:684px;top:24px;width:150px;height:96px;">
  <div class="brand" style="position:absolute;left:10px;top:10px;font-size:5px;">
    <span class="brand__dot"></span>Harlow Hauling
  </div>
  <div class="tagline" style="position:absolute;left:10px;top:18px;">Fine furniture transport and delivery service</div>
  <svg class="wave" viewBox="0 0 150 16" height="16" preserveAspectRatio="none">
    <path d="M0 8 Q70 0 150 7 V16 H0Z" fill="var(--green)"/>
    <path d="M0 12 Q80 5 150 11 V16 H0Z" fill="var(--charcoal)"/>
  </svg>
</div>

<!-- Compliment slip 2 -->
<div class="sheet compliment-slip" style="left:684px;top:134px;width:150px;height:96px;">
  <div class="brand" style="position:absolute;left:10px;top:10px;font-size:5px;">
    <span class="brand__dot"></span>Harlow Hauling
  </div>
  <div class="tagline" style="position:absolute;left:10px;top:18px;">Fine furniture transport and delivery service</div>
  <svg class="wave" viewBox="0 0 150 16" height="16" preserveAspectRatio="none">
    <path d="M0 8 Q70 0 150 7 V16 H0Z" fill="var(--green)"/>
    <path d="M0 12 Q80 5 150 11 V16 H0Z" fill="var(--charcoal)"/>
  </svg>
</div>

<!-- Envelope back (dark) -->
<div class="sheet sheet--dark envelope" style="left:852px;top:24px;width:180px;height:84px;">
  <svg class="flap" viewBox="0 0 180 84" height="84" preserveAspectRatio="none">
    <path d="M0 0 L90 40 L180 0Z" fill="var(--charcoal-dark)"/>
  </svg>
  <div class="brand" style="position:absolute;left:50%;top:34px;transform:translateX(-50%);font-size:5px;">
    <span class="brand__dot"></span>Harlow Hauling
  </div>
</div>

<!-- Envelope back (green) -->
<div class="sheet envelope" style="left:876px;top:74px;width:180px;height:84px;background:var(--green);">
  <svg class="flap" viewBox="0 0 180 84" height="84" preserveAspectRatio="none">
    <path d="M0 0 L90 40 L180 0Z" fill="var(--green-deep)"/>
  </svg>
  <div class="brand" style="position:absolute;left:50%;top:34px;transform:translateX(-50%);font-size:5px;color:var(--paper);">
    <span class="brand__dot" style="background:var(--paper);"></span>Harlow Hauling
  </div>
</div>

<!-- Envelope front (white) -->
<div class="sheet envelope" style="left:868px;top:170px;width:180px;height:84px;">
  <div class="brand" style="position:absolute;left:8px;top:8px;font-size:4.5px;">
    <span class="brand__dot"></span>Harlow Hauling
  </div>
  <div class="contact" style="position:absolute;left:8px;top:16px;font-size:2.8px;">
    5810 County Road 7, Canaan, NH 03598
  </div>
  <svg class="wave" viewBox="0 0 180 12" height="12" preserveAspectRatio="none">
    <path d="M0 6 Q90 0 180 6 V12 H0Z" fill="var(--green)"/>
  </svg>
</div>

</body>
</html>
```